Web Design - home page mockup + 5 sub pages

K7 Teardown & Clearing is an industry leading demolition company in Edmonton, Alberta. Recently awarded the 2013 Builder of the Season award for its focus on social and environmental responsibility, K7 is committed to training employees so that they have real-world skills in demolition, which gives K7 the ability to divert construction waste from landfills back into use.
The website needs to appeal to non-tech savvy general contractors who want quick answers regarding the kinds of demolition projects that K7 can take on. So flashy or ultra glitchy designs are off track.
As the project title states, the home page links to 5 primary sub-pages through the use of navigation and "banners". The home page should have a feature slider as well as calls to action for the general contractor and property manager (without saying 'general contractor'). See this example (http://patternmart.example/item/vast-agile-adaptive-company-skin/full_screen_preview/8274193). When I say 'banner' that could be an [image+title+excerpt] like the two 1/2 columns in the example.
One small section of the home page should be a banner about the 2013 award. And one section for blog posts.
K7 Clear wants an engaging, yet clean corporate feel that isn't saturated with the "eco-friendly" / "green" look. One section,"The Den” (name still under going revision) should have a more personal/organic look that is sufficiently different from the other sub-pages as it is not directly related to the business services.
Main Navigation: Home | Selective Demolition | Tenant Improvement | The K7 Edge | Our Team | The Den | In The News | Contact Us |
I will purchase a premium WordPress theme from a service like PatternMart, and then integrate the design into the WordPress theme, the designer need only create the mockups, and then deliver the cut up Photoshop/Illustrator files.

Current website - http://www.k7clearco.example/
**UPDATE JULY 15**
Just uploaded the logo and award image. Please ensure that the "O" in T-ULM-A matches the logo itself. Half the "O" is the light green and half the "O" is the darker darker green with the arrows. "ULM" itself should be green, with the caveat mentioned above. Thank you.
=================================================
Examples of what we're looking for:
Main Nav look, but too much wasted space in the header - http://patternmart.example/item/vast-agile-adaptive-company-skin/full_screen_preview/8274193
4 banners "pop out" & Nice section headers - http://gravonix.example/saga/
efficient use of space & clean design - http://patternmart.example/item/kelvo-sharp-adaptive-allround-skin/full_screen_preview/8261507
Meet The Team - http://www.pramix.example/demo/quarvex/pages/meet-the-team/

Hello Designers,

I just uploaded the logo and award images as .eps files.  Please note: The "O" in T-ULM-A should match the logo itself.  Half the "O" is light green, half the "O" is dark green and has the arrow end caps in opposite directions. Thanks.

We will be selecting a design by end of day wednesday.  Please submit a design proposal by then to be included in the selection process. Our goal is have a design nearly completed by end of day Friday (July 19).  Thanks for all your submissions to date.

Designers, we will be selecting a designer within the next two days. Please submit designs as soon as possible.  Thank you.

Reason: Its taking a long time between getting designs from designers and getting feedback from client. Need more time to finalize home page and then turning to sub pages.

Requirements
Must have
• Visually communicate the priority of K7 on social responsibility & sustainability without using "green" branding or images.
On home page, "Selective Demolition" & "Tenant Improvement" & "2013 Builder of the Season" Award should pop out immediately.
This is a demolition company first and foremost, which leverages standard projects to introduce principles of the triple bottom line.
Nice to have
• A design palette with colors, fonts, and styles.
Designed to easily integrate with a premium wordpress theme

```html
<!DOCTYPE html>
<html lang="en">
<head>
<meta charset="utf-8">
<title>K7 Teardown &amp; Clearing – About Us</title>
<link href="https://fonts.googleapis.com/css2?family=Oswald:wght@300;400;600&family=Russo+One&family=Arimo:wght@400;700&display=swap" rel="stylesheet">
<style>
:root{
  --teal:#0b6468;
  --lime:#8dc63f;
  --red:#e2231a;
  --text:#333;
  --grey:#8a8a8a;
  --footer:#efefef;
  --bar:#dcdcdc;
}
*{box-sizing:border-box;margin:0;padding:0}
html,body{width:880px;height:1200px;overflow:hidden;background:#fff;font-family:Arimo,Arial,sans-serif;color:var(--text)}
.page{position:relative;width:880px;height:1200px;overflow:hidden}
.brand{position:absolute;left:18px;top:10px;display:flex;align-items:center;gap:14px}
.brand-mark{width:104px;height:104px;border-radius:50%;border:9px solid var(--lime)}
.brand-name{font-family:Oswald,sans-serif;font-weight:400;font-size:19px;color:var(--teal);line-height:1.15;width:170px}
.contact{position:absolute;top:40px;display:flex;align-items:center;gap:6px;color:var(--teal)}
.contact svg{width:44px;height:44px;flex:none}
.contact-main{font-family:Oswald,sans-serif;font-weight:300;font-size:27px;line-height:1;white-space:nowrap}
.contact-sub{font-size:9.5px;margin-top:3px;white-space:nowrap}
.phone{left:360px}.mail{left:634px}
.nav{position:absolute;left:0;top:124px;width:880px;height:34px;border-bottom:4px solid var(--lime);display:flex;padding-left:16px}
.nav a{font-family:Oswald,sans-serif;font-weight:300;font-size:17px;color:var(--teal);text-decoration:none;padding:3px 16px 0;height:30px;border-right:1px solid #b9d98f;white-space:nowrap}
.nav a:last-child{border:none}
.nav a.active{border-bottom:4px solid var(--red);height:34px}
.hero{position:absolute;left:0;top:158px;width:880px;height:155px;background:linear-gradient(180deg,#c9b89a 0%,#8a8f6a 35%,#2e3540 75%,#3b3a38 100%)}
.about{position:absolute;left:48px;top:355px;width:796px;font-size:12.3px;line-height:15.8px}
.avatar-space{float:left;width:249px;height:290px}
.avatar{position:absolute;left:22px;top:11px;width:176px;height:176px;border-radius:50%;border:4px solid var(--lime);background:#ebf2e1}
.about h1{font-family:"Russo One",sans-serif;font-weight:400;font-size:32px;color:var(--teal);margin:4px 0 8px;line-height:36px}
.about p{margin-bottom:13px}
.footer{position:absolute;left:0;top:867px;width:880px;height:284px;background:var(--footer);border-top:6px solid var(--bar)}
.footer-art{position:absolute;left:40px;top:60px;width:820px;height:224px;background:linear-gradient(90deg,#dcdcdc,#e9e9e9 40%,#ececec 70%,#e8d6c6);opacity:.8}
.footer h2{position:absolute;top:28px;font-family:Oswald,sans-serif;font-weight:600;font-size:23px;color:var(--red);letter-spacing:-.3px;white-space:nowrap}
.col-nav{left:37px}.col-qc{left:362px}.col-lc{left:675px}
.links{position:absolute;top:72px;list-style:none;font-size:11px;line-height:15.8px}
.links.one{left:37px}
.links.two{left:165px;width:160px;text-transform:uppercase;color:#555}
.links.two li{padding-left:14px;position:relative;margin-bottom:9px;line-height:12px}
.links.two li::before{content:"";position:absolute;left:0;top:2px;border:4px solid transparent;border-left:6px solid #555}
.field{position:absolute;left:359px;width:234px;height:24px;border-radius:9px;background:var(--grey);color:#fff;font-size:9.5px;font-weight:700;padding:7px 16px}
.message{height:90px}
.send{position:absolute;left:530px;top:223px;width:60px;height:26px;border-radius:3px;background:#a9a9a9;color:#fff;font-size:10.5px;font-weight:700;text-align:center;padding-top:7px}
.social{position:absolute;left:674px;top:71px;display:flex;gap:9px}
.social span{width:24px;height:24px;border-radius:50%;background:var(--lime)}
.news{position:absolute;left:678px;top:111px;font-size:9.5px;color:#555;line-height:11.5px}
.subfield{left:677px;top:155px;width:163px;height:23px}
.subscribe{position:absolute;left:680px;top:190px;font-size:9.5px;font-weight:700;color:#666}
.foot-phone{position:absolute;left:674px;top:212px;display:flex;align-items:center;gap:4px;color:var(--teal);font-family:Oswald,sans-serif;font-weight:300;font-size:23px;white-space:nowrap}
.bottom{position:absolute;left:0;top:1151px;width:880px;height:49px;background:var(--bar);font-size:11px;padding:20px 32px}
.mini-brand{position:absolute;right:30px;top:12px;display:flex;align-items:center;gap:6px;font-size:8px;color:#555}
.mini-brand span{width:28px;height:28px;border-radius:50%;border:2px solid #444}
</style>
</head>
<body>
<div class="page">
  <header>
    <div class="brand"><div class="brand-mark"></div><div class="brand-name">K7 Teardown &amp; Clearing</div></div>
    <div class="contact phone">
      <svg viewBox="0 0 44 44"><circle cx="22" cy="22" r="19.5" fill="none" stroke="#8dc63f" stroke-width="3"/><path d="M15 12c2-1 3 0 4 3s0 4-1 5c1 3 3 5 6 7 1-1 2-2 4-1s4 2 3 4-3 3-5 2c-7-3-11-8-13-14-1-3 0-5 2-6z" fill="#8dc63f"/></svg>
      <div><div class="contact-main">1-555-0142736</div><div class="contact-sub">38 street address • Mon-Fri 8 am - 6 pm</div></div>
    </div>
    <div class="contact mail">
      <svg viewBox="0 0 44 44"><circle cx="22" cy="22" r="19.5" fill="none" stroke="#8dc63f" stroke-width="3"/><rect x="11" y="14" width="22" height="15" fill="#8dc63f"/><path d="M11 14l11 9 11-9" fill="none" stroke="#fff" stroke-width="1.6"/></svg>
      <div><div class="contact-main">info@k7.example</div><div class="contact-sub">name of city • Sat 9 am - 4 pm</div></div>
    </div>
    <nav class="nav">
      <a href="#">Home</a><a href="#">Selective Demolition</a><a href="#">Tenant Improvement</a><a href="#">The K7 Edge</a><a href="#" class="active">Our Team</a><a href="#">The Den</a><a href="#">In The News</a><a href="#">Contact Us</a>
    </nav>
  </header>
  <div class="hero" role="img" aria-label="Team photo of the crew in hard hats and safety vests in front of a work truck"></div>

  <main class="about">
    <div class="avatar-space"></div>
    <div class="avatar" role="img" aria-label="Team member portrait placeholder"></div>
    <h1>ABOUT US</h1>
    <p>Lorem ipsum dolor sit amet, consectetur adipisicing elit, sed do eiusmod tempor incididunt ut labore et dolore magna aliqua. Ut enim ad minim veniam, quis nostrud exercitation ullamco laboris nisi ut aliquip ex ea commodo consequat. Duis aute irure dolor in reprehenderit in voluptate velit esse cillum dolore eu fugiat nulla pariatur. Excepteur sint occaecat cupidatat non proident, sunt in culpa qui officia deserunt mollit anim id est laborum.</p>
    <p>&nbsp;Sed ut perspiciatis, unde omnis iste natus error sit voluptatem accusantium doloremque laudantium, totam rem aperiam eaque ipsa, quae ab illo inventore veritatis et quasi architecto beatae vitae dicta sunt, explicabo. Nemo enim ipsam voluptatem, quia voluptas sit, aspernatur aut odit aut fugit, sed quia consequuntur magni dolores eos, qui ratione voluptatem sequi nesciunt, neque porro quisquam est, qui dolorem ipsum, quia dolor sit amet, consectetur, adipisci[ng] velit, sed quia non numquam eius modi tempora inci[di]dunt, ut labore et dolore magnam aliquam quaerat voluptatem. Ut enim ad minima veniam, quis nostrum exercitationem ullam corporis suscipit laboriosam, nisi ut aliquid ex ea commodi consequatur? Quis autem vel eum iure reprehenderit, qui in ea voluptate velit esse, quam nihil molestiae consequatur, vel illum, qui dolorem eum fugiat, quo voluptas nulla pariatur?</p>
    <p>At vero eos et accusamus et iusto odio dignissimos ducimus, qui blanditiis praesentium voluptatum deleniti atque corrupti, quos dolores et quas molestias excepturi sint, obcaecati cupiditate non provident, similique sunt in culpa, qui officia deserunt mollitia animi, id est laborum et dolorum fuga. Et harum quidem rerum facilis est et expedita distinctio. Nam libero tempore, cum soluta nobis est eligendi optio, cumque nihil impedit, quo minus id, quod maxime placeat, facere possimus, omnis voluptas assumenda est, omnis dolor repellendus.</p>
  </main>

  <footer class="footer">
    <div class="footer-art" role="img" aria-label="Faded background scene of workers on a lift and a telehandler machine"></div>
    <h2 class="col-nav">NAVIGATION</h2>
    <ul class="links one"><li>Home</li><li>Selective Demolition</li><li>Tenant Improvement</li><li>The K7 Edge</li><li>Our Team</li><li>The Den</li><li>In The News</li><li>Contact Us</li></ul>
    <ul class="links two"><li>Selective Demolition</li><li>Tenant Improvement</li><li>2013 Builder<br>of the Season</li></ul>
    <h2 class="col-qc">QUICK CONTACT</h2>
    <div class="field" style="top:64px">full name</div>
    <div class="field" style="top:92px">email address</div>
    <div class="field message" style="top:121px"></div>
    <div class="send">send</div>
    <h2 class="col-lc">LETS CONNECT</h2>
    <div class="social"><span></span><span></span><span></span><span></span><span></span></div>
    <div class="news">subscribe to our monthly newsletter<br>and get the best deals and discounts</div>
    <div class="field subfield">enter email address</div>
    <div class="subscribe">➤&nbsp; subscribe now</div>
    <div class="foot-phone"><svg width="24" height="24" viewBox="0 0 44 44"><circle cx="22" cy="22" r="19.5" fill="none" stroke="#0b6468" stroke-width="3"/><path d="M15 12c2-1 3 0 4 3s0 4-1 5c1 3 3 5 6 7 1-1 2-2 4-1s4 2 3 4-3 3-5 2c-7-3-11-8-13-14-1-3 0-5 2-6z" fill="#0b6468"/></svg>1-555-0142736</div>
  </footer>
  <div class="bottom">© 2013 K7 Teardown &amp; Clearing. All Rights Reserved 2013
    <div class="mini-brand"><span></span>K7 Clear</div>
  </div>
</div>
</body>
</html>
```